New small software startup needs a web design!

Hi! I need a talented web designer to design the overall visual look & feel & navigation of my website.
Just images and basic HTML of course; this is a website design contest not so much a coding contest (although using PHP for "include()" etc might be good!), although yes I have paid the extra $150 for a "Coded Website"

GENERAL OVERVIEW:
-----------------
My new startup company is very simple - I develop and sell shareware apps for Windows.
The software I develop is low-level system & security, so keep that in mind when designing the look & feel of the website.
My website which you are designing for is for hosting the company and showcasing the software.

So it's not a very complicated website, and has a very basic layout/structure.

Most of the webpages I need you to design will essentially just have "blank content" of course, so you don't need to worry about many technicalities, mostly just the LOOK & FEEL & NAVIGATION.

So as you can probably already imagine, it needs things like:
- Download page
- Shop page where they can click links to purchase
- About page where they can read FAQ/Privacy Policy/Terms Of Use, or Contact me
- Members area for registered users to login, where they can download and get tech support
- a subdirectory for each software application to show each off on its own (eg. /software/app1/index.htm)
- a page where i can offer a one-page summary of my products in different foreign languages

IMPORTANT:
----------
- HTML4 ONLY (no HTML5)
- Must support Firefox, Internet Explorer, and Chrome
- CSS is good, although you dont have to use it if you dont want to or feel it's unnecessary
- NO ACTIVE CONTENT (no Flash or Java etc)
- NO SCRIPTS (no Javascript or VBScript etc)
- The overall type of look/feel i'm after is "CLEAN, PROFESSIONAL, TECHNICAL" (but not overcomplicated)
- You must incorporate the company logo - see Attached file.
(You're free to use Photoshop etc to modify the logo how you see fit, for example to resize its elements, or to change the location of the company name part of it, or to remove part of it, change background/transparency, etc etc)
- Although ive named all files here .HTM i'll actually be using PHP, so feel free to use .PHP names also, but .HTM is fine also
- You're also free to use server-side PHP if you wish, for example to include() files such as footer.htm
- Please use Photoshop for designing the images - i'll naturally be needing all PSD files
- Please only use fonts that can be used commercially. The font we use in our logo is 'Good Times' in case you're wondering, although I'm not suggesting one way or the other to use it or not for the website - just because it looks good in the logo may not necessarily mean it works for the rest of the website. Then again, maybe it does, i dont know.

BASIC WEBSITE DIRECTORY STRUCTURE:
----------------------------------
These are the files you should be sending me. Most of these can just be essentially blank pages in regards to content (or with some "dummy filler" text/images), although most (including most "blanks") will obviously have hyperlinks to other pages.
But obviously each page even the blank ones will still have main menu etc.

In no particular order:
---
/index.htm "Welcome to Quellvane..."
/books/index.htm "Select a book category..."
/books/cat1/index.htm - List of books in cat1
/books/cat2/index.htm - List of books in cat2
/members.htm Username & pass login page. Also acts as the Unsuccessful page.
/members/index.htm - Successfully logged in
/members/download.htm - Members-only downloads
/members/support.htm - Members-only support (basically just a clone of /about/contact.htm)
/about/index.htm "About Quellvane..."
/about/contact.htm "Contact Us..."
/about/privacy.htm "Privacy Statement"
/about/termsofuse.htm "Terms of Use"
/about/resellers.htm "Information for Resellers"
/lang/index.htm "Select language..."
/lang/fr/index.htm - French products summary page
/lang/es/index.htm - Spanish products summary page
/software/index.htm "Select a program to find out more about it..."
/software/support.htm "Technical support"
/software/shop.htm "Select a program to buy..."
/software/download.htm "Select a program to download..."
/software/app1/index.htm Main "About" page for Application #1
/software/app1/download.htm - Download page for App 1
/software/app1/features.htm - Features page for App 1
/software/app1/screenshots.htm - Screenshots page for App 1
/software/app1/support.htm - Support page for App 1
/software/app1/purchase.htm - Purchase page for App 1
/software/app2/index.htm (clone of App 1)
/software/app2/download.htm "
/software/app2/screenshots.htm "
/software/app2/support.htm "
/software/app2/purchase.htm "
/misc/footer.htm A footer that all other pages also include() -- see below for details

---

MAIN MENU (available from every page):
Home (/index.htm)
Software (/software/index.htm)
Shop (/software/shop.htm)
Books (/books/index.htm)
Members (/members.htm)
Resellers (/about/resellers.htm)
Support (/software/support.htm)
About (/about/index.htm)

FOOTER (every page) for the smallprint:
"Copyright (C) 2015. All rights reserved."
as well as hyperlinks to "Privacy Policy", "Terms of Use", "Contact"

MEMBERS AREA:
The Members subarea also has an extra submenu:
Home (/members/index.htm)
Download (/members/download.htm)
Support (/members/support.htm)

APPLICATION AREA:
Each Application subarea also has an extra submenu:
Home (/software/app1/index.htm)
Features (/software/app1/features.htm)
Download (/software/app1/download.htm)
Support (/software/app1/support.htm)
Purchase (/software/app1/purchase.htm)
Screenshots (/software/app1/screenshots.htm)

Obviously it would be best to have one single FOOTER.HTM that every other HTM file can link to, rather than having the footer in every file (I'll be using PHP so its easy to "include(footer.htm)")

--
Thankyou for taking on my design challenge, and I wish you best of luck and a great design! :)

Target Market(s)

General users of Windows operating system who use system & security tools

Industry/Entity Type

Computer Software

Coding

Coded - Design and coding required

Number of Pages Required

5+ page

Font styles to use
Serif
Sans Serif

Requirements
Must have
• See project description
Should not have
• See project description

```html
<!DOCTYPE html>
<html lang="en">
<head>
<meta charset="utf-8">
<title>Quellvane — System &amp; Security Software</title>
<link rel="stylesheet" href="https://fonts.googleapis.com/css2?family=Open+Sans:wght@400;600;700;800&display=swap">
<style>
:root{
  --blue:#1f6fb8;
  --blue-bright:#2b86d3;
  --blue-deep:#175a98;
  --red:#d8342c;
  --slate:#3d4650;
  --ink:#333a40;
  --muted:#8a9098;
  --line:#dfe3e7;
  --soft:#f1f4f7;
  --footer:#1d2228;
  --footer-deep:#14181c;
  --white:#ffffff;
}
*{box-sizing:border-box;margin:0;padding:0}
html,body{width:1200px;height:2608px;overflow:hidden}
body{font-family:"Open Sans",Arial,sans-serif;color:var(--ink);background:var(--white);font-size:12px;line-height:1.6}
.wrap{width:800px;margin:0 auto;position:relative}
ul{list-style:none}

/* header */
.site-header{height:80px}
.site-header .wrap{height:80px;display:flex;align-items:center;justify-content:space-between}
.brand{display:flex;align-items:center;gap:8px;color:var(--blue);font-weight:800;font-size:18px;letter-spacing:1px}
.brand-dot{width:18px;height:18px;border-radius:50%;background:var(--blue-bright)}
.header-tools{display:flex;flex-direction:column;align-items:flex-end;gap:6px}
.login-btn{background:var(--blue);color:var(--white);font-size:10px;font-weight:700;padding:2px 12px;border-radius:2px}
.search{width:150px;height:20px;border:1px solid var(--line);border-radius:10px;display:flex;align-items:center;justify-content:flex-end;padding-right:6px}

/* nav */
.main-nav{height:32px}
.main-nav ul{width:800px;margin:0 auto;height:32px;background:var(--blue);display:flex}
.main-nav li{flex:1;color:var(--white);font-size:11px;font-weight:700;text-transform:uppercase;text-align:center;line-height:32px}
.main-nav li.active{background:var(--red);flex:0 0 90px}

/* hero */
.hero{height:288px}
.hero .wrap{height:288px;background:linear-gradient(90deg,var(--blue-deep) 0%,var(--blue-bright) 48%,#cfe0ee 70%,#e9eef2 100%);overflow:hidden}
.hero-photo{position:absolute;right:0;top:0;width:400px;height:288px;background:radial-gradient(ellipse at 60% 45%,#f4efe9 0%,#c9d6e2 55%,rgba(120,160,200,0) 100%)}
.hero-swoosh{position:absolute;left:0;top:0}
.hero-copy{position:absolute;left:32px;top:78px;width:330px;color:var(--white)}
.hero-copy h1{font-size:30px;font-weight:800;letter-spacing:.5px;line-height:1.1;margin-bottom:10px}
.hero-copy p{font-size:12px;font-weight:600;margin-bottom:18px}
.btn{display:inline-block;font-size:11px;font-weight:700;border-radius:3px;padding:5px 16px}
.btn-light{background:var(--white);color:var(--blue)}
.btn-blue{background:var(--blue);color:var(--white)}
.btn-ghost{border:1px solid var(--white);color:var(--white);padding:4px 14px}

/* what we do */
.services{height:340px;background:linear-gradient(180deg,#fff 0%,var(--soft) 100%)}
.section-title{text-align:center;font-size:22px;font-weight:600;color:var(--ink);text-transform:uppercase}
.section-intro{width:560px;margin:8px auto 0;text-align:center;color:var(--muted);font-size:11px;line-height:1.5}
.services .section-title{padding-top:28px}
.service-grid{display:flex;justify-content:space-between;width:620px;margin:36px auto 0}
.service{width:140px;text-align:center}
.service-icon{width:52px;height:52px;border-radius:50%;border:2px solid var(--blue-bright);margin:0 auto 8px;display:flex;align-items:center;justify-content:center}
.service-icon.filled{background:var(--blue)}
.service h3{font-size:10px;font-weight:700;color:var(--ink);text-transform:uppercase;line-height:1.3;margin-bottom:6px}
.service p{font-size:9px;color:var(--muted);line-height:1.5;margin-bottom:10px}

/* feature columns */
.features{height:240px;padding-top:12px}
.features .wrap{display:flex;height:216px}
.feature-col{flex:1;padding:22px 26px;color:var(--white)}
.feature-col.blue{background:var(--blue-bright)}
.feature-col.dark{background:var(--slate)}
.feature-col h2{font-size:18px;font-weight:700;text-transform:uppercase;margin-bottom:12px}
.tick-list li{font-size:10px;line-height:20px;display:flex;align-items:center;gap:8px}
.feature-col .btn{margin-top:12px}
.feature-col.dark p{font-size:10px;line-height:1.5;margin:6px 0 0 20px}

/* showcase */
.showcase{height:490px}
.showcase .section-title{padding-top:32px}
.showcase-grid{display:flex;justify-content:space-between;margin-top:36px}
.card{width:256px}
.card-media{height:184px;border:1px solid var(--line)}
.card h3{font-size:11px;font-weight:700;color:var(--blue);text-transform:uppercase;margin:12px 0 4px}
.card p{font-size:9px;color:var(--muted);line-height:1.55}
.card-arrow{margin-top:14px;width:20px;height:20px;border-radius:50%;border:1px solid var(--blue-bright);display:flex;align-items:center;justify-content:center}

/* testimonials */
.testimonials{height:430px;padding-top:30px}
.testimonials .wrap{height:380px;background:linear-gradient(180deg,#4a7cb6 0%,#6b95c6 60%,#8aaad0 100%);color:var(--white);text-align:center;padding-top:26px}
.testimonials .section-title{color:var(--white)}
.testimonials .section-intro{color:#e4edf7;width:600px}
.quotes{display:flex;justify-content:space-between;width:660px;margin:34px auto 0}
.quote{width:180px}
.avatar{width:64px;height:64px;border-radius:50%;margin:0 auto 10px;background:radial-gradient(circle at 50% 40%,#e8d9cc 0%,#9aa7b4 70%);border:3px solid rgba(255,255,255,.6)}
.quote p{font-size:9px;line-height:1.55;color:#eef3f9}
.quote-mark{font-size:34px;font-weight:700;line-height:1;margin-top:14px;color:var(--white)}

/* clients */
.clients{height:260px}
.clients .section-title{padding-top:34px}
.client-row{display:flex;justify-content:space-between;width:760px;margin:34px auto 0}
.client{width:140px;height:70px;border:1px solid var(--line);box-shadow:0 2px 4px rgba(0,0,0,.08);display:flex;align-items:center;justify-content:center;gap:6px;font-size:14px;font-weight:700;color:var(--blue-deep)}
.client-dot{width:10px;height:10px;background:var(--blue-bright);border-radius:50%}

/* footer */
.site-footer{height:448px;background:var(--footer);color:#aab2ba;position:relative}
.footer-cols{display:flex;justify-content:space-between;width:1000px;margin:0 auto;padding-top:40px}
.footer-col{width:200px}
.footer-col h4{color:var(--white);font-size:11px;font-weight:700;text-transform:uppercase;margin-bottom:12px}
.footer-col li{font-size:10px;line-height:22px}
.footer-col li::before{content:"› ";color:var(--blue-bright)}
.footer-col p{font-size:10px;line-height:1.5;margin-bottom:10px}
.field{height:22px;background:#2a3037;border:1px solid #39414a;margin-bottom:8px;font-size:9px;padding:3px 8px;color:#7d868f}
.social{display:flex;gap:8px;margin-bottom:22px}
.social span{width:24px;height:24px;border-radius:50%;background:#39424b}
.footer-brand{color:var(--white);font-size:15px;font-weight:800;letter-spacing:1px;display:flex;align-items:center;gap:6px}
.footer-bar{position:absolute;left:0;bottom:0;width:1200px;height:40px;background:var(--footer-deep);text-align:center;font-size:10px;line-height:40px;color:#8a939c}
.footer-bar a{color:#c2cad2;text-decoration:none}
</style>
</head>
<body>

<header class="site-header">
  <div class="wrap">
    <div class="brand"><span class="brand-dot"></span>QUELLVANE</div>
    <div class="header-tools">
      <span class="login-btn">LOGIN</span>
      <div class="search">
        <svg width="10" height="10" viewBox="0 0 10 10"><circle cx="4" cy="4" r="3" fill="none" stroke="#8a9098" stroke-width="1.3"/><line x1="6.2" y1="6.2" x2="9.2" y2="9.2" stroke="#8a9098" stroke-width="1.3"/></svg>
      </div>
    </div>
  </div>
</header>

<nav class="main-nav">
  <ul>
    <li class="active">Home</li><li>Features</li><li>Download</li><li>Support</li><li>Purchase</li><li>Screenshots</li>
  </ul>
</nav>

<section class="hero">
  <div class="wrap">
    <div class="hero-photo" role="img" aria-label="Photo of a support engineer wearing a headset at a computer"></div>
    <svg class="hero-swoosh" width="800" height="288" viewBox="0 0 800 288"><path d="M420 288 C470 200 520 140 600 100" fill="none" stroke="rgba(255,255,255,.35)" stroke-width="6"/></svg>
    <div class="hero-copy">
      <h1>LOREM IPSUM</h1>
      <p>Lorem Ipsum is simply dummy text of the printing and typesetting industry. Lorem Ipsum has been the industry's standard dummy text ever since.</p>
      <span class="btn btn-light">More info</span>
    </div>
  </div>
</section>

<section class="services">
  <h2 class="section-title">What we do</h2>
  <p class="section-intro">Lorem Ipsum is simply dummy text of the printing and typesetting industry. Lorem Ipsum has been the industry's standard dummy text ever since the printer took a galley of type and scrambled it.</p>
  <div class="service-grid">
    <div class="service">
      <div class="service-icon"><svg width="24" height="24" viewBox="0 0 24 24"><path d="M6 17h12a4 4 0 0 0 0-8 6 6 0 0 0-11.5 1.5A3.5 3.5 0 0 0 6 17z" fill="none" stroke="#2b86d3" stroke-width="1.8"/></svg></div>
      <h3>Simply<br>dummy text</h3>
      <p>Lorem ipsum dolor sit amet, consectetur adipiscing elit, sed do eiusmod tempor incididunt labore.</p>
      <span class="btn btn-blue">Read More</span>
    </div>
    <div class="service">
      <div class="service-icon filled"><svg width="24" height="24" viewBox="0 0 24 24"><rect x="3" y="4" width="18" height="12" rx="1" fill="none" stroke="#fff" stroke-width="1.8"/><line x1="9" y1="20" x2="15" y2="20" stroke="#fff" stroke-width="1.8"/></svg></div>
      <h3>Simply<br>dummy text</h3>
      <p>Lorem ipsum dolor sit amet, consectetur adipiscing elit, sed do eiusmod tempor incididunt labore.</p>
      <span class="btn btn-blue">Read More</span>
    </div>
    <div class="service">
      <div class="service-icon"><svg width="24" height="24" viewBox="0 0 24 24"><path d="M12 3 C8 9 6 12 6 15a6 6 0 0 0 12 0c0-3-2-6-6-12z" fill="none" stroke="#2b86d3" stroke-width="1.8"/></svg></div>
      <h3>Simply<br>dummy text</h3>
      <p>Lorem ipsum dolor sit amet, consectetur adipiscing elit, sed do eiusmod tempor incididunt labore.</p>
      <span class="btn btn-blue">Read More</span>
    </div>
    <div class="service">
      <div class="service-icon"><svg width="24" height="24" viewBox="0 0 24 24"><circle cx="12" cy="12" r="4" fill="none" stroke="#2b86d3" stroke-width="1.8"/><circle cx="12" cy="12" r="8.5" fill="none" stroke="#2b86d3" stroke-width="1.8" stroke-dasharray="3 2.4"/></svg></div>
      <h3>Simply<br>dummy text</h3>
      <p>Lorem ipsum dolor sit amet, consectetur adipiscing elit, sed do eiusmod tempor incididunt labore.</p>
      <span class="btn btn-blue">Read More</span>
    </div>
  </div>
</section>

<section class="features">
  <div class="wrap">
    <div class="feature-col blue">
      <h2>Lorem ipsum is simply dummy text</h2>
      <ul class="tick-list">
        <li><svg width="12" height="12" viewBox="0 0 12 12"><circle cx="6" cy="6" r="6" fill="#fff"/><path d="M3 6l2 2 4-4" fill="none" stroke="#2b86d3" stroke-width="1.6"/></svg>Lorem ipsum is simply dummy text</li>
        <li><svg width="12" height="12" viewBox="0 0 12 12"><circle cx="6" cy="6" r="6" fill="#fff"/><path d="M3 6l2 2 4-4" fill="none" stroke="#2b86d3" stroke-width="1.6"/></svg>Lorem ipsum is simply dummy text</li>
        <li><svg width="12" height="12" viewBox="0 0 12 12"><circle cx="6" cy="6" r="6" fill="#fff"/><path d="M3 6l2 2 4-4" fill="none" stroke="#2b86d3" stroke-width="1.6"/></svg>Lorem ipsum is simply dummy text printing</li>
        <li><svg width="12" height="12" viewBox="0 0 12 12"><circle cx="6" cy="6" r="6" fill="#fff"/><path d="M3 6l2 2 4-4" fill="none" stroke="#2b86d3" stroke-width="1.6"/></svg>Lorem ipsum is simply dummy text of</li>
        <li><svg width="12" height="12" viewBox="0 0 12 12"><circle cx="6" cy="6" r="6" fill="#fff"/><path d="M3 6l2 2 4-4" fill="none" stroke="#2b86d3" stroke-width="1.6"/></svg>Lorem ipsum is simply dummy text</li>
      </ul>
      <span class="btn btn-ghost">Read More</span>
    </div>
    <div class="feature-col dark">
      <h2>Lorem ipsum is simply</h2>
      <ul class="tick-list">
        <li><svg width="12" height="12" viewBox="0 0 12 12"><path d="M2 6l3 3 5-6" fill="none" stroke="#fff" stroke-width="1.8"/></svg>Lorem ipsum is simply dummy text of print</li>
        <li><svg width="12" height="12" viewBox="0 0 12 12"><path d="M2 6l3 3 5-6" fill="none" stroke="#fff" stroke-width="1.8"/></svg>Lorem ipsum is simply dummy text of print</li>
        <li><svg width="12" height="12" viewBox="0 0 12 12"><path d="M2 6l3 3 5-6" fill="none" stroke="#fff" stroke-width="1.8"/></svg>Lorem ipsum is simply dummy text</li>
      </ul>
      <p>Lorem ipsum is simply dummy text of the printing and typesetting industry. Lorem Ipsum has been the standard.</p>
      <span class="btn btn-ghost">Read More</span>
    </div>
  </div>
</section>

<section class="showcase">
  <div class="wrap">
    <h2 class="section-title">Lorem ipsum is simply dummy text</h2>
    <p class="section-intro">Lorem Ipsum is simply dummy text of the printing and typesetting industry. Lorem Ipsum has been the industry's standard dummy text ever since the 1500s, when an unknown printer took a galley of type.</p>
    <div class="showcase-grid">
      <div class="card">
        <div class="card-media" role="img" aria-label="Photo of a hand pointing at a data chart on a screen" style="background:linear-gradient(135deg,#9db9d6,#2b6aa8)"></div>
        <h3>Lorem ipsum simply</h3>
        <p>Lorem Ipsum is simply dummy text of the printing and typesetting industry. Lorem Ipsum has been the standard dummy text ever since.</p>
        <div class="card-arrow"><svg width="8" height="8" viewBox="0 0 8 8"><path d="M2 1l3 3-3 3" fill="none" stroke="#2b86d3" stroke-width="1.4"/></svg></div>
      </div>
      <div class="card">
        <div class="card-media" role="img" aria-label="Photo of a keyboard with a service key" style="background:linear-gradient(135deg,#8c9095,#3a3f45)"></div>
        <h3>Lorem ipsum simply</h3>
        <p>Lorem Ipsum is simply dummy text of the printing and typesetting industry. Lorem Ipsum has been the standard dummy text ever since.</p>
        <div class="card-arrow"><svg width="8" height="8" viewBox="0 0 8 8"><path d="M2 1l3 3-3 3" fill="none" stroke="#2b86d3" stroke-width="1.4"/></svg></div>
      </div>
      <div class="card">
        <div class="card-media" role="img" aria-label="Photo of business people shaking hands" style="background:linear-gradient(135deg,#e6e9ec,#7d8792)"></div>
        <h3>Lorem ipsum simply</h3>
        <p>Lorem Ipsum is simply dummy text of the printing and typesetting industry. Lorem Ipsum has been the standard dummy text ever since.</p>
        <div class="card-arrow"><svg width="8" height="8" viewBox="0 0 8 8"><path d="M2 1l3 3-3 3" fill="none" stroke="#2b86d3" stroke-width="1.4"/></svg></div>
      </div>
    </div>
  </div>
</section>

<section class="testimonials">
  <div class="wrap" role="img" aria-label="Testimonials band over a soft blue city photo">
    <h2 class="section-title">Testimonials</h2>
    <p class="section-intro">Lorem Ipsum is simply dummy text of the printing and typesetting industry. Lorem Ipsum has been the industry's standard dummy text ever since the 1500s, when an unknown printer took a galley.</p>
    <div class="quotes">
      <div class="quote">
        <div class="avatar" role="img" aria-label="Portrait photo of a customer"></div>
        <p>Lorem Ipsum is simply dummy text of the printing and typesetting industry. Lorem Ipsum has been the standard text ever since.</p>
        <div class="quote-mark">&ldquo;</div>
      </div>
      <div class="quote">
        <div class="avatar" role="img" aria-label="Portrait photo of a customer"></div>
        <p>Lorem Ipsum is simply dummy text of the printing and typesetting industry. Lorem Ipsum has been the standard text ever since.</p>
        <div class="quote-mark">&ldquo;</div>
      </div>
      <div class="quote">
        <div class="avatar" role="img" aria-label="Portrait photo of a customer"></div>
        <p>Lorem Ipsum is simply dummy text of the printing and typesetting industry. Lorem Ipsum has been the standard text ever since.</p>
        <div class="quote-mark">&ldquo;</div>
      </div>
    </div>
  </div>
</section>

<section class="clients">
  <h2 class="section-title">Our client</h2>
  <div class="client-row">
    <div class="client"><span class="client-dot"></span>Norvale</div>
    <div class="client">Tidecrest</div>
    <div class="client">Bytemoor</div>
    <div class="client">Company Name</div>
    <div class="client">Ironpeak</div>
  </div>
</section>

<footer class="site-footer">
  <div class="footer-cols">
    <div class="footer-col">
      <h4>Main menu</h4>
      <ul><li>Home</li><li>Software</li><li>Shop</li><li>Books</li><li>Members</li><li>Resellers</li></ul>
    </div>
    <div class="footer-col">
      <h4>Quick links</h4>
      <ul><li>Company Policy</li><li>Purchase</li><li>Terms and conditions of use</li><li>Special support</li><li>Site map</li></ul>
    </div>
    <div class="footer-col">
      <h4>Newsletter</h4>
      <p>Lorem ipsum dolor sit amet, sign up for news.</p>
      <div class="field">Your name</div>
      <div class="field">Email id</div>
      <span class="btn btn-blue">Send</span>
    </div>
    <div class="footer-col">
      <h4>Get in touch</h4>
      <div class="social" aria-label="Social links"><span></span><span></span><span></span></div>
      <div class="footer-brand"><span class="brand-dot"></span>QUELLVANE</div>
    </div>
  </div>
  <div class="footer-bar">Copyright (C) 2015. All rights reserved. &nbsp;|&nbsp; <a>Privacy Policy</a> &nbsp;|&nbsp; <a>Terms of Use</a> &nbsp;|&nbsp; <a>Contact</a></div>
</footer>

</body>
</html>
```